Business card por a urban DJ, up scale audience target

Need a sober design, modern, conservative colors but i can consider some options, y play rnb, hip hop, EDM and top40.

Business card for contact and personal info, double sided, use logo attrached please; im 42 so i need a card acording to my age an target audience.

Target Market(s)

Adult people, up scale audience

Industry/Entity Type

Music Download

Contact Information for Business Card

Cel (574) 3209415586 www.lumaverso.com

Requirements
Must have
• open mind
Nice to have
• open mind
Should not have
• DJ

```html
<!DOCTYPE html>
<html lang="en">
<head>
<meta charset="utf-8">
<title>Business Card – Luma</title>
<link rel="stylesheet" href="https://fonts.googleapis.com/css2?family=Open+Sans:wght@400;600;800&display=swap">
<style>
  :root{
    --page:#5b5c5f;
    --card-deep:#0f1b24;
    --card-mid:#1c2b36;
    --card-light:#4d5c68;
    --band:#13212b;
    --bokeh-a:#2a3d4b;
    --bokeh-b:#5f8a90;
    --text-main:#e6ecef;
    --text-soft:#9fb0ba;
  }
  *{box-sizing:border-box;margin:0;padding:0}
  html,body{width:1200px;height:734px;overflow:hidden}
  body{
    background:var(--page);
    font-family:"Open Sans",Arial,sans-serif;
    position:relative;
  }
  .card{
    position:absolute;
    top:224px;
    width:500px;
    height:286px;
    overflow:hidden;
    box-shadow:0 6px 18px rgba(0,0,0,.35);
  }
  /* logo side */
  .card--brand{
    left:67px;
    background:linear-gradient(180deg,var(--card-deep) 0%,var(--card-mid) 45%,var(--card-light) 100%);
    display:flex;
    align-items:center;
    justify-content:center;
    gap:14px;
  }
  .brand-mark{
    width:22px;height:22px;background:var(--text-main);
  }
  .brand-name{
    color:var(--text-main);
    font-weight:800;
    font-size:78px;
    letter-spacing:4px;
    line-height:1;
  }
  /* contact side */
  .card--contact{
    left:633px;
    background:var(--card-deep);
  }
  .card__lights{
    position:absolute;
    left:0;top:0;width:100%;height:130px;
    background:
      radial-gradient(ellipse at 70% 40%,var(--bokeh-b) 0%,transparent 55%),
      linear-gradient(180deg,var(--bokeh-a),var(--card-deep));
    opacity:.9;
  }
  .card__band{
    position:absolute;
    left:0;top:118px;width:86%;height:168px;
    background:linear-gradient(180deg,var(--band),#0c1820);
  }
  .holder-name{
    position:absolute;
    left:28px;top:92px;
    color:var(--text-main);
    font-weight:600;
    font-size:22px;
    letter-spacing:.5px;
  }
  .contact-list{
    position:absolute;
    left:28px;top:140px;
    list-style:none;
  }
  .contact-list li{
    display:flex;align-items:center;gap:9px;
    color:var(--text-soft);
    font-size:10px;
    line-height:20px;
  }
  .contact-list svg{width:10px;height:10px;fill:var(--text-soft)}
  .genres{
    position:absolute;
    left:0;width:86%;bottom:30px;
    text-align:center;
    color:var(--text-soft);
    font-weight:600;
    font-size:9px;
    letter-spacing:1px;
  }
</style>
</head>
<body>

<section class="card card--brand" aria-label="Card front">
  <span class="brand-mark"></span>
  <span class="brand-name">LUMA</span>
</section>

<section class="card card--contact" aria-label="Card back">
  <div class="card__lights" role="img" aria-label="Soft teal bokeh lights"></div>
  <div class="card__band"></div>
  <h1 class="holder-name">Your Name</h1>
  <ul class="contact-list">
    <li>
      <svg viewBox="0 0 10 10"><path d="M0 2h10v6H0z M0 2l5 3.5L10 2" stroke="#0f1b24" stroke-width=".8"/></svg>
      hello@lumaverso.com
    </li>
    <li>
      <svg viewBox="0 0 10 10"><circle cx="2" cy="8" r="1.3"/><path d="M1 5a4 4 0 0 1 4 4h-1.2A2.8 2.8 0 0 0 1 6.2z M1 2a7 7 0 0 1 7 7H6.8A5.8 5.8 0 0 0 1 3.2z"/></svg>
      www.lumaverso.com
    </li>
    <li>
      <svg viewBox="0 0 10 10"><path d="M2 0.5l2 2-1 1.3a6 6 0 0 0 3.2 3.2l1.3-1 2 2-1.2 1.5C5 9.5 0.5 5 0.5 1.7z"/></svg>
      (574) 3209415586
    </li>
  </ul>
  <p class="genres">R&amp;B HIP HOP EDM</p>
</section>

</body>
</html>
```